Electrical Industry Newletter Design Project PSD format with layers

The Name of the newsletter is:
A "Pulse" of the Hour
-This is a bi monthly newsletter focused on the Electrical and Cabling Industry
"Pulse" of course is a play on words referring to a Sine wave
We are looking for a creative yet professional looking newsletter. Our targeted audience are professional consulting engineers, architects, & property owners/manager.
We are looking for a unique logo for the newsletters name "Pull of the Hours" with the subtext being "Electrical & Cabling Industry"
We envision the incorporations of the sin wave into the logo and other such associated symbols associated with our industry.
Note: the Newsletter is going to be brought to them by our company KAV Electric. Our logo should be incorporated near the top of the newsletter but be less prominent.
Each issue is going to be a "Vol" Hence the Vol number should be editable.
There should be a featured article area labeled
-Whats Happening
-This section should have a spot for a relevant pictures
There should be a side section labeled
-Code Alert!
-Just for laughs
-This section should be available to place a relevant picture or comic strips of sorts.
The should be a section labeled
-Project Profile (This will be where we profile a recent project with pictures
You have total artistic license with this project, I know you will produce a great work of art!
Updates
What happened to all those creative juices??? Added Thursday, April 27, 2017
Target Market(s)
Consulting Engineers, Architects, Specifiers, Building Owners & Managers
Industry/Entity Type
Electrical
Look and feel

```html
<!DOCTYPE html>
<html lang="en">
<head>
<meta charset="utf-8">
<title>Pulse of the Hours Newsletter</title>
<link href="https://fonts.googleapis.com/css2?family=PT+Sans:ital,wght@0,400;0,700;1,400&family=PT+Sans+Narrow:wght@700&display=swap" rel="stylesheet">
<style>
:root{
  --yellow:#f5b700;
  --dark:#3b3b3b;
  --ink:#2e2e2e;
  --red:#ec1c24;
  --white:#ffffff;
  --text:#3a3a3a;
  --photo-blue:#5f86ad;
}
*{margin:0;padding:0;box-sizing:border-box}
html,body{width:1200px;height:3666px;overflow:hidden}
body{position:relative;background:var(--white);font-family:"PT Sans",Arial,sans-serif;color:var(--text)}
.abs{position:absolute}
.masthead-title{left:55px;top:48px;font-weight:700;font-size:62px;line-height:58px;color:var(--ink);font-family:"PT Sans",Arial,sans-serif}
.masthead-mark{left:55px;top:56px;width:0;height:0}
.masthead-sub{left:55px;top:158px;font-weight:700;font-style:italic;font-size:27px;color:var(--yellow);letter-spacing:1px}
.vol{left:601px;top:0;width:125px;height:139px;background:var(--yellow);color:var(--white);text-align:center;font-weight:700;line-height:1}
.vol .label{display:block;font-size:26px;padding-top:10px}
.vol .num{display:block;font-size:48px}
.vol .date{display:block;font-size:15px;padding-top:4px}
.sponsor{left:810px;top:30px;width:355px;text-align:right}
.sponsor .by{font-size:16px;color:var(--ink)}
.sponsor .company{display:flex;justify-content:flex-end;align-items:center;gap:10px;margin-top:6px;font-weight:700;font-size:28px;color:var(--ink)}
.sponsor .company i{width:22px;height:22px;background:var(--ink);display:block}
.shapes{left:0;top:0}
.section-tag{background:var(--yellow);color:var(--ink);font-weight:700;font-family:"PT Sans Narrow","PT Sans",sans-serif;display:flex;align-items:center;justify-content:center}
.happening-tag{left:823px;top:254px;width:340px;height:93px;font-size:34px}
.happening{left:49px;top:366px;width:1102px;color:#f0f0f0;font-size:17.5px;line-height:25px;text-align:justify}
.happening p{text-indent:22px;margin-bottom:14px}
.happening .accent{color:var(--yellow)}
.happening h3{color:var(--yellow);font-size:19px;margin:0 0 4px 22px}
.happening .quote{color:var(--yellow);font-style:italic}
.btn{background:var(--yellow);color:var(--ink);font-weight:700;font-size:15px;display:flex;align-items:center;justify-content:center}
.btn-happening{left:49px;top:819px;width:139px;height:61px}
.photo-strip{left:0;top:860px;width:1200px;height:448px;display:flex;clip-path:polygon(0 87px,100% 0,100% 100%,0 100%)}
.photo{display:block}
.featured-tag{left:909px;top:868px;width:240px;height:61px;font-size:22px}
.alert-box{left:0;top:1393px;width:240px;height:279px;background:var(--red)}
.alert-text{left:276px;top:1393px;width:560px;font-style:italic;font-size:17px;line-height:24px;color:var(--ink)}
.alert-badge{left:868px;top:1371px;width:234px;height:234px;border-radius:50%;background:var(--red);color:var(--white);font-weight:700;font-family:"PT Sans Narrow","PT Sans",sans-serif;font-size:50px;line-height:50px;display:flex;align-items:center;justify-content:center;text-align:center}
.laughs-photo{left:49px;top:1723px;width:477px;height:538px;background:linear-gradient(160deg,#d9d2c8,#3f4656 70%,#2b303a)}
.laughs-title{left:700px;top:1805px;width:463px;text-align:right;font-family:"PT Sans Narrow","PT Sans",sans-serif;font-weight:700;font-size:44px;color:var(--ink)}
.laughs-text{left:618px;top:1887px;width:531px;font-size:18px;line-height:25px;color:var(--ink);text-align:justify}
.profile-tag{left:860px;top:2327px;width:262px;height:259px;background:var(--dark);color:var(--white);font-family:"PT Sans Narrow","PT Sans",sans-serif;font-weight:700;font-size:42px;line-height:50px;display:flex;align-items:center;justify-content:center;text-align:center}
.profile-lead{left:49px;top:2392px;width:782px;font-style:italic;font-size:17.5px;line-height:25px;text-align:justify;color:var(--ink)}
.profile-lead p{text-indent:22px}
.profile-body{left:49px;top:2635px;width:1102px;font-size:17.5px;line-height:25px;color:var(--ink);text-align:justify}
.profile-body p{text-indent:22px;margin-bottom:22px}
.profile-body .quote{color:var(--red);font-style:italic}
.btn-profile{left:535px;top:2901px;width:140px;height:61px}
.gallery{left:0;top:2987px;width:1200px;height:618px;display:grid;grid-template-columns:398px 388px 398px;grid-template-rows:306px 305px;gap:7px 8px}
.footer{left:0;top:3605px;width:1200px;height:61px;background:var(--dark);color:#d8d8d8;text-align:center;font-size:14px;line-height:20px;padding-top:9px}
.footer .contact{color:var(--yellow)}
.footer .links{color:#ffffff}
.blue{background:linear-gradient(180deg,#7ea3c8,#3f6a96 60%,#a9b9c8)}
.warm{background:linear-gradient(160deg,#efe9e2,#484d58 75%)}
.tech{background:linear-gradient(135deg,#2c4a66,#89a4b8 55%,#c7b8a8)}
</style>
</head>
<body>

<svg class="abs shapes" width="1200" height="3666" viewBox="0 0 1200 3666" aria-hidden="true">
  <polygon points="0,232 1200,183 1200,870 0,945" fill="#3b3b3b"/>
  <polygon points="0,228 1200,179 1200,186 0,235" fill="#f5b700"/>
  <polygon points="0,934 1200,858 1200,870 0,946" fill="#f5b700"/>
  <polygon points="0,1822 1200,1711 1200,2090 0,2212" fill="#f5b700"/>
</svg>

<header>
  <div class="abs masthead-title">pulse of the hours<br>NEWSLETTER</div>
  <div class="abs masthead-sub">ELECTRICAL &amp; CABLING INDUSTRY</div>
  <div class="abs vol"><span class="label">VOL</span><span class="num">01</span><span class="date">MARCH<br>2017</span></div>
  <div class="abs sponsor">
    <div class="by">brought to you by</div>
    <div class="company"><i></i>KAV ELECTRIC LLC</div>
  </div>
</header>

<section class="whats-happening">
  <div class="abs section-tag happening-tag">WHAT'S HAPPENING</div>
  <div class="abs happening">
    <p>Lorem ipsum dolor sit amet, consectetur adipiscing elit. Donec id interdum ante, non vulputate elit. Aenean magna augue, ultricies vel condimentum vel, volutpat non urna. Phasellus tincidunt arcu porttitor massa aliquam ultrices. Integer condimentum in risus ut molestie. Vivamus at diam ornare ligula iaculis rutrum. Proin lacinia nisl eu pellentesque aliquet. Nam id elit sagittis, dapibus dui nec, vestibulum risus. Duis vel aliquam dui, vitae luctus est. Proin nibh est, euismod sit amet ornare sit amet, suscipit id erat. <span class="accent">Duis id sem eros.</span> Sed et dignissim ex.</p>
    <h3>HEADLINE</h3>
    <p>Nulla dignissim ornare eleifend. Curabitur in rhoncus tellus, a scelerisque enim. Pellentesque tempor consequat diam, nec sagittis nibh. Vivamus hendrerit scelerisque euismod. Etiam placerat tristique ligula, quis iaculis neque hendrerit pharetra. Integer sit amet nulla maximus, vulputate turpis rhoncus, condimentum ligula. Nulla quis rutrum quam. In hac habitasse platea dictumst.</p>
    <p class="quote">Sed eget ante et sem fringilla convallis vitae vel massa. Sed maximus faucibus metus, id eleifend arcu malesuada et. Praesent enim lacus, euismod sit amet dui non, feugiat viverra lectus. Sed quis augue arcu. Etiam sed suscipit urna, ac maximus elit. Praesent faucibus, nulla suscipit tempus egestas, lacus neque lobortis est, ac eleifend enim nibh sed eros. Lorem ipsum dolor sit amet, consectetur adipiscing elit.</p>
  </div>
  <div class="abs btn btn-happening">READ MORE</div>
</section>

<section class="featured-photos">
  <div class="abs photo-strip">
    <div class="photo tech" style="width:335px" role="img" aria-label="Photo of network cables plugged into a patch panel"></div>
    <div class="photo blue" style="width:398px" role="img" aria-label="Photo of a steel transmission tower against a blue sky"></div>
    <div class="photo blue" style="width:467px" role="img" aria-label="Photo of a bright industrial warehouse interior"></div>
  </div>
  <div class="abs section-tag featured-tag">FEATURED PHOTOS</div>
</section>

<section class="code-alert">
  <svg class="abs alert-box" viewBox="0 0 240 279" role="img" aria-label="Exclamation mark">
    <rect x="0" y="0" width="240" height="279" fill="#ec1c24"/>
    <polygon points="100,50 140,50 134,180 106,180" fill="#fff"/>
    <rect x="102" y="200" width="36" height="34" fill="#fff"/>
  </svg>
  <div class="abs alert-text">
    Lorem ipsum dolor sit amet, consectetur adipiscing elit. Integer bibendum eros in diam aliquet, et commodo dolor venenatis. Nulla eleifend sapien sit amet odio imperdiet efficitur. Interdum et malesuada fames ac ante ipsum primis in faucibus. Cras eget massa lorem.<br>
    Quisque augue enim, pellentesque nec mi vitae, tincidunt gravida lectus. Cras facilisis varius iaculis. Nunc turpis tortor, blandit eget tristique et, dapibus sit amet dolor.<br>
    Nam at maximus tellus. In hac habitasse platea dictumst. Sed maximus eget leo ac vulputate. Morbi hendrerit mauris et nunc varius, vitae aliquet eros dictum.
  </div>
  <div class="abs alert-badge">CODE<br>ALERT</div>
</section>

<section class="just-for-laughs">
  <div class="abs laughs-photo" role="img" aria-label="Photo of a laughing man in a dark blazer"></div>
  <h2 class="abs laughs-title">JUST FOR LAUGHS</h2>
  <div class="abs laughs-text">
    Lorem ipsum dolor sit amet, consectetur adipiscing elit. Integer bibendum eros in diam aliquet, et commodo dolor venenatis. Nulla eleifend sapien sit amet odio imperdiet efficitur. Interdum et malesuada fames ac ante ipsum primis in faucibus. Cras eget massa lorem.<br>
    Quisque augue enim, pellentesque nec mi vitae, tincidunt gravida lectus. Cras facilisis varius iaculis. Nunc turpis tortor, blandit eget tristique et, dapibus sit amet dolor. ullamcorper.<br>
    Morbi nec fringilla sem.
  </div>
</section>

<section class="project-profile">
  <div class="abs profile-tag">PROJECT<br>PROFILE</div>
  <div class="abs profile-lead"><p>Lorem ipsum dolor sit amet, consectetur adipiscing elit. Donec id interdum ante, non vulputate elit. Aenean magna augue, ultricies vel condimentum vel, volutpat non urna. Phasellus tincidunt arcu porttitor massa aliquam ultrices. Integer condimentum in risus ut molestie. Vivamus at diam ornare ligula iaculis rutrum. Proin lacinia nisl eu pellentesque aliquet. Nam id elit sagittis, dapibus dui nec, vestibulum risus. Duis vel aliquam dui, vitae luctus est. Proin nibh est, euismod sit amet ornare sit amet, suscipit id erat. Duis id sem eros. Sed et dignissim ex.</p></div>
  <div class="abs profile-body">
    <p>Nulla dignissim ornare eleifend. Curabitur in rhoncus tellus, a scelerisque enim. Pellentesque tempor consequat diam, nec sagittis nibh. Vivamus hendrerit scelerisque euismod. Etiam placerat tristique ligula, quis iaculis neque hendrerit pharetra. Integer sit amet nulla maximus, vulputate turpis rhoncus, condimentum ligula. Nulla quis rutrum quam. In hac habitasse platea dictumst.</p>
    <p class="quote">Sed eget ante et sem fringilla convallis vitae vel massa. Sed maximus faucibus metus, id eleifend arcu malesuada et. Praesent enim lacus, euismod sit amet dui non, feugiat viverra lectus. Sed quis augue arcu. Etiam sed suscipit urna, ac maximus elit. Praesent faucibus, nulla suscipit tempus egestas, lacus neque lobortis est, ac eleifend enim nibh sed eros. Lorem ipsum dolor sit amet, consectetur adipiscing elit.</p>
  </div>
  <div class="abs btn btn-profile">READ MORE</div>
  <div class="abs gallery">
    <div class="blue" role="img" aria-label="Photo of a warehouse loading bay"></div>
    <div class="warm" role="img" aria-label="Photo of a smiling man in a blazer"></div>
    <div class="tech" role="img" aria-label="Photo of hands working at an electrical control panel"></div>
    <div class="warm" role="img" aria-label="Photo of a laughing man in a blazer"></div>
    <div class="tech" role="img" aria-label="Photo of a technician operating test equipment"></div>
    <div class="blue" role="img" aria-label="Photo of an industrial hall interior"></div>
  </div>
</section>

<footer class="abs footer">
  <div class="contact">KAV Electric, llc 214 Harlow Street, Brookfield, New Jersey 07990 &nbsp;&nbsp; Phone: 555-014-2923 &nbsp;Fax: 555-014-2958 &nbsp;info@kavelectric-example.com</div>
  <div class="links">Unsubscribe | Manage Email Preferences</div>
</footer>

</body>
</html>
```